Business Card Design Project

I require a business card for a new coaching business based in Melbourne with global clients. Both companies and individuals will retain our coaching services.

Target Market(s)

Both small business and large corporate in western speaking countries. Individuals requiring support and direction on issues such as fears, phobias, career, relationships, confidence, self esteem etc.

Industry/Entity Type

Business

Font styles to use
Sans Serif

Colors

Designer to choose colors to be used in the design.

Requirements
Must have
• White background to enhance the colours in the logo. Logo on the left.
Should not have
• The black and white version of the logo. Keep the colours.

```html
<!DOCTYPE html>
<html lang="en">
<head>
<meta charset="utf-8">
<title>Clear Path Coaching – Business Card</title>
<link rel="stylesheet" href="https://fonts.googleapis.com/css2?family=Roboto:wght@400;500;700&display=swap">
<style>
  :root {
    --page-bg: #ffffff;
    --card-bg: #ffffff;
    --card-edge: #d9d9d9;
    --panel-grey: #c4c2c3;
    --panel-text: #ffffff;
    --ink-grey: #7a7879;
    --brand-accent: #e0177f;
    --card-shadow: 3px 4px 5px rgba(0, 0, 0, 0.45);
  }
  * { box-sizing: border-box; margin: 0; padding: 0; }
  html, body {
    width: 1060px;
    height: 1200px;
    overflow: hidden;
    background: var(--page-bg);
    font-family: "Roboto", Arial, sans-serif;
  }
  .canvas { position: relative; width: 1060px; height: 1200px; }

  .card {
    position: absolute;
    background: var(--card-bg);
    border: 1px solid var(--card-edge);
    box-shadow: var(--card-shadow);
    overflow: hidden;
  }

  /* Front */
  .card-front { left: 211px; top: 126px; width: 620px; height: 376px; }
  .brand-side {
    position: absolute; left: 0; top: 0; width: 311px; height: 100%;
    display: flex; flex-direction: column; align-items: center;
  }
  .brand-mark { margin-top: 60px; width: 150px; height: 150px; }
  .brand-name {
    margin-top: 40px;
    color: var(--ink-grey);
    font-weight: 500;
    font-size: 24px;
    line-height: 30px;
    letter-spacing: 0.5px;
    text-align: center;
    text-transform: uppercase;
  }
  .contact-panel {
    position: absolute; left: 311px; top: 0; right: 0; bottom: 0;
    background: var(--panel-grey);
    color: var(--panel-text);
    text-align: center;
  }
  .person-name { position: absolute; top: 231px; width: 100%; font-size: 22px; font-weight: 400; }
  .person-role { position: absolute; top: 260px; width: 100%; font-size: 16px; }
  .contact-list { position: absolute; top: 300px; width: 100%; list-style: none; font-size: 14px; line-height: 19.5px; }

  /* Back */
  .card-back { left: 223px; top: 666px; width: 629px; height: 381px; }
  .tagline {
    position: absolute; left: 0; right: 0; top: 125px;
    text-align: center;
    color: var(--ink-grey);
    font-size: 27px;
    line-height: 31px;
    font-weight: 400;
    letter-spacing: 0.3px;
  }
  .tagline strong { font-weight: 700; }
</style>
</head>
<body>
<main class="canvas">
  <section class="card card-front" aria-label="Business card front">
    <div class="brand-side">
      <svg class="brand-mark" viewBox="0 0 150 150" aria-hidden="true">
        <circle cx="75" cy="75" r="56" fill="var(--brand-accent)"/>
      </svg>
      <p class="brand-name">Clear Path<br>Coaching</p>
    </div>
    <div class="contact-panel">
      <h1 class="person-name">Maren Castell-Hoyt</h1>
      <p class="person-role">Performance Consultant and Coach</p>
      <ul class="contact-list">
        <li>Phone +61 (0) 400 555 019</li>
        <li>Email&nbsp; maren.c@example.com</li>
        <li>ABN 10987654321</li>
      </ul>
    </div>
  </section>

  <section class="card card-back" aria-label="Business card back">
    <p class="tagline">
      The <strong>mind is more powerful</strong><br>
      than the body.<br>
      Give yourself permission<br>
      to <strong>shine.</strong>
    </p>
  </section>
</main>
</body>
</html>
```